Brisk Tissu, wipes multipack branding 3 types in 1 family

Brisk Tissu is a wipe producing company. For some information see our (not completed) website at briskissu.nl. We also have a product named Palmora (see Palmora.com).
Our philosophy is to produce environmental friendly wipes only. We are doing that by using both bamboo and 100% bioviscose as Nonwoven. Both are biodegradable and compostable. We produce single packed wipes and multipacks (think about hygiene for hand, deodorant wipes and playtime wipes (for cleaning sex toys)). We are looking for designs for our multipacks (6 to 10 pieces per package). The size of the unfolded package foil is about 150 x 190mm (width x height) (but varies depending on the material and the number of wipes).
The branding should be modern, fresh and in line with our thoughts.

We want to have 3 packages designed for:
- Purely2Palms multipack 6 pieces
- Deodorant wipes multipack 6 pieces
- Playtime wipes multipack 10 pieces
All should have the look and feel of our Brisk Tissu logo / branding, and belong to the same family of products (to be recognised they belong together).

I added our logo as well as some examples of other packages we have been creating as samples. At first we have been thinking about using that design for multipacks as well, but we were not that happy about that.
Please consider them as a style that we liked.

Target Market(s)

Consumers
- Festival people (Purely2Palms and Deodorant)
- Adults with children (Purely2Palms)
- Travelers (Purely2Palm and Deodorant)
- Business people (Deodorant)
- Erotic industry (Playtime wipes)

Font styles to use
Sans Serif

Colors

Designer to choose colors to be used in the design.

Requirements
Must have
• A family in branding, recognisability as being part of 1 family of products.
• Branded with our logo (as attached).
• Necessary and mandatory information on the back of the package.
Nice to have
• Designs that fit to the purpose of the wipes.
• Different Colors for the different products.
• Chosen font is just because it is modern. Could be any other modern font as well.
Should not have
• Old fashioned style.
• Too much focus on the "green-ness" of the products.

```html
<!DOCTYPE html>
<html lang="en">
<head>
<meta charset="utf-8">
<title>Brisk Tissu – multipack family</title>
<link rel="stylesheet" href="https://fonts.googleapis.com/css2?family=Open+Sans:wght@400;700&family=Arimo:wght@400&display=swap">
<style>
  :root {
    --canvas: #f5f5f5;
    --white: #ffffff;
    --deo: #e3173f;
    --deo-dark: #c9102f;
    --deo-ink: #3a0a12;
    --hands: #1f2553;
    --hands-dark: #181d45;
    --play: #7a2477;
    --play-dark: #671d64;
    --window: rgba(200, 200, 205, 0.55);
  }
  * { box-sizing: border-box; margin: 0; padding: 0; }
  html, body { width: 1200px; height: 519px; overflow: hidden; background: var(--canvas); }
  .canvas { position: relative; width: 1200px; height: 519px; }

  .pack {
    position: absolute; top: 58px; width: 323px; height: 408px;
    background: linear-gradient(90deg, var(--pack) 0, var(--pack) 160px, var(--white) 323px);
    color: var(--white);
    font-family: "Arimo", Arial, sans-serif;
  }
  .pack--deo { left: 53px; --pack: var(--deo); --pack-dark: var(--deo-dark); }
  .pack--hands { left: 444px; top: 54px; --pack: var(--hands); --pack-dark: var(--hands-dark); }
  .pack--play { left: 830px; top: 54px; --pack: var(--play); --pack-dark: var(--play-dark); }

  .pack__fade {
    position: absolute; left: 160px; top: 0; width: 163px; height: 100%;
    background: linear-gradient(90deg, var(--pack) 0%, rgba(255,255,255,0) 100%);
    opacity: 0.35;
  }

  .pack__story {
    position: absolute; left: 33px; top: 44px; width: 170px;
    font-size: 5.6px; line-height: 6px;
  }
  .pack--deo .pack__story,
  .pack--deo .pack__maker,
  .pack--deo .pack__ingredients { color: var(--deo-ink); }

  .pack__care { position: absolute; left: 65px; top: 105px; }

  .pouch {
    position: absolute; left: 8px; top: 116px; width: 304px; height: 172px;
    background: linear-gradient(90deg, var(--pack-dark) 0, var(--pack-dark) 150px, var(--window) 210px, var(--window) 100%);
    color: var(--white);
  }
  .brand {
    position: absolute; left: 0; width: 162px; top: 36px;
    display: flex; align-items: center; justify-content: center; gap: 5px;
    font-family: "Open Sans", sans-serif; font-weight: 700; font-size: 8.5px;
    letter-spacing: 0.6px; line-height: 9px;
  }
  .brand__mark { width: 9px; height: 9px; border-radius: 50%; background: var(--white); }
  .product {
    position: absolute; left: 0; width: 162px; top: 62px; text-align: center;
    font-family: "Open Sans", sans-serif;
  }
  .product__name { font-weight: 700; font-size: 24px; line-height: 28px; white-space: nowrap; }
  .product__name--long { font-size: 18px; }
  .product__claim { font-size: 8.5px; line-height: 11px; margin-top: 1px; }
  .pouch__icons { position: absolute; left: 56px; top: 128px; }

  .pack__maker {
    position: absolute; left: 33px; top: 300px; width: 180px;
    font-size: 5.6px; line-height: 6.4px;
  }
  .pack__maker .best { margin-top: 7px; }
  .pack__ingredients {
    position: absolute; left: 33px; top: 348px; width: 160px;
    font-size: 4.8px; line-height: 5.4px;
  }
  .pack__date-slot {
    position: absolute; left: 15px; top: 364px; width: 8px; height: 21px;
    background: rgba(255,255,255,0.75);
  }
  .seal {
    position: absolute; left: 200px; top: 310px; width: 48px; height: 48px;
    border-radius: 50%; background: var(--white); border: 2px solid var(--pack);
  }
</style>
</head>
<body>
<main class="canvas">

  <section class="pack pack--deo">
    <div class="pack__fade" role="img" aria-label="Halftone diamond dot pattern fading from pack colour to white"></div>
    <div class="pack__story">
      <p>Deo wipe for women</p>
      <p>Wet bio deo wipe for that fresh feeling<br>even at the end of the day.<br>Enter your last meeting of the day with a fresh<br>and clean feeling.<br>Fresh yourself with these soft<br>and careful wipes and experience the gentle feeling.<br>For all occasions where you need refreshment.<br>While traveling, working, sporting or just to prepare<br>for your date.</p>
    </div>
    <svg class="pack__care" width="50" height="10" viewBox="0 0 50 10" fill="none" stroke="#fff" stroke-width="1">
      <path d="M1 3 q2 -2 4 0 t4 0 M1 7 q2 -2 4 0 t4 0"/>
      <circle cx="26" cy="5" r="4"/>
      <path d="M36 2 h6 M37 3 l1 6 h3 l1 -6"/>
    </svg>
    <div class="pouch">
      <div class="brand"><span class="brand__mark"></span>BRISK TISSU</div>
      <div class="product">
        <p class="product__name">DEO WIPE</p>
        <p class="product__claim">For women<br>Biodegradable</p>
      </div>
      <svg class="pouch__icons" width="50" height="12" viewBox="0 0 50 12" fill="none" stroke="#fff" stroke-width="0.9">
        <path d="M6 11 V6 M6 6 q-4 0 -5 -4 q4 0 5 4 q1 -4 5 -4 q-1 4 -5 4"/>
        <path d="M23 11 V2 M23 5 q-3 -1 -4 -3 M23 7 q3 -1 4 -3"/>
        <circle cx="42" cy="6" r="3.2"/><path d="M42 0.5v2 M42 9.5v2 M36.5 6h2 M45.5 6h2"/>
      </svg>
    </div>
    <div class="pack__maker">
      <p>BRISK TISSU</p>
      <p>Made in the EU, designed by Brisk Tissu BV,<br>P.O. Box 4120, 7411KB Zutphen - The Netherlands</p>
      <p class="best">Best used before the end of:</p>
    </div>
    <div class="pack__ingredients">
      <p>Ingredients</p>
      <p>Aqua, Aluminum Chlorohydrate, Propylene Glycol,<br>PEG-40 Hydrogenated Castor Oil, Ethylhexylglycerin,<br>Octenidine HCl, Phenoxyethanol, Parfum, Limonene.</p>
    </div>
    <div class="pack__date-slot"></div>
    <div class="seal" role="img" aria-label="Organic badge"></div>
  </section>

  <section class="pack pack--hands">
    <div class="pack__fade" role="img" aria-label="Halftone diamond dot pattern fading from pack colour to white"></div>
    <div class="pack__story">
      <p>Deo wipe for women</p>
      <p>Wet bio deo wipe for that fresh feeling<br>even at the end of the day.<br>Enter your last meeting of the day with a fresh<br>and clean feeling.<br>Fresh yourself with these soft<br>and careful wipes and experience the gentle feeling.<br>For all occasions where you need refreshment.<br>While traveling, working, sporting or just to prepare<br>for your date.</p>
    </div>
    <svg class="pack__care" width="50" height="10" viewBox="0 0 50 10" fill="none" stroke="#fff" stroke-width="1">
      <path d="M1 3 q2 -2 4 0 t4 0 M1 7 q2 -2 4 0 t4 0"/>
      <circle cx="26" cy="5" r="4"/>
      <path d="M36 2 h6 M37 3 l1 6 h3 l1 -6"/>
    </svg>
    <div class="pouch">
      <div class="brand"><span class="brand__mark"></span>BRISK TISSU</div>
      <div class="product">
        <p class="product__name product__name--long">PURELY2PALMS</p>
        <p class="product__claim">With antibacterial effectiveness<br>Biodegradable</p>
      </div>
      <svg class="pouch__icons" width="50" height="12" viewBox="0 0 50 12" fill="none" stroke="#fff" stroke-width="0.9">
        <path d="M6 11 V6 M6 6 q-4 0 -5 -4 q4 0 5 4 q1 -4 5 -4 q-1 4 -5 4"/>
        <path d="M23 11 V2 M23 5 q-3 -1 -4 -3 M23 7 q3 -1 4 -3"/>
        <circle cx="42" cy="6" r="3.2"/><path d="M42 0.5v2 M42 9.5v2 M36.5 6h2 M45.5 6h2"/>
      </svg>
    </div>
    <div class="pack__maker">
      <p>BRISK TISSU</p>
      <p>Made in the EU, designed by Brisk Tissu BV,<br>P.O. Box 4120, 7411KB Zutphen - The Netherlands</p>
      <p class="best">Best used before the end of:</p>
    </div>
    <div class="pack__ingredients">
      <p>Ingredients</p>
      <p>Aqua, Aluminum Chlorohydrate, Propylene Glycol,<br>PEG-40 Hydrogenated Castor Oil, Ethylhexylglycerin,<br>Octenidine HCl, Phenoxyethanol, Parfum, Limonene.</p>
    </div>
    <div class="pack__date-slot"></div>
    <div class="seal" role="img" aria-label="Organic badge"></div>
  </section>

  <section class="pack pack--play">
    <div class="pack__fade" role="img" aria-label="Halftone diamond dot pattern fading from pack colour to white"></div>
    <div class="pack__story">
      <p>Deo wipe for women</p>
      <p>Wet bio deo wipe for that fresh feeling<br>even at the end of the day.<br>Enter your last meeting of the day with a fresh<br>and clean feeling.<br>Fresh yourself with these soft<br>and careful wipes and experience the gentle feeling.<br>For all occasions where you need refreshment.<br>While traveling, working, sporting or just to prepare<br>for your date.</p>
    </div>
    <svg class="pack__care" width="50" height="10" viewBox="0 0 50 10" fill="none" stroke="#fff" stroke-width="1">
      <path d="M1 3 q2 -2 4 0 t4 0 M1 7 q2 -2 4 0 t4 0"/>
      <circle cx="26" cy="5" r="4"/>
      <path d="M36 2 h6 M37 3 l1 6 h3 l1 -6"/>
    </svg>
    <div class="pouch">
      <div class="brand"><span class="brand__mark"></span>BRISK TISSU</div>
      <div class="product">
        <p class="product__name product__name--long">JOY RINSE WIPE</p>
        <p class="product__claim">With antibacterial effectiveness<br>Biodegradable</p>
      </div>
      <svg class="pouch__icons" width="50" height="12" viewBox="0 0 50 12" fill="none" stroke="#fff" stroke-width="0.9">
        <path d="M6 11 V6 M6 6 q-4 0 -5 -4 q4 0 5 4 q1 -4 5 -4 q-1 4 -5 4"/>
        <path d="M23 11 V2 M23 5 q-3 -1 -4 -3 M23 7 q3 -1 4 -3"/>
        <circle cx="42" cy="6" r="3.2"/><path d="M42 0.5v2 M42 9.5v2 M36.5 6h2 M45.5 6h2"/>
      </svg>
    </div>
    <div class="pack__maker">
      <p>BRISK TISSU</p>
      <p>Made in the EU, designed by Brisk Tissu BV,<br>P.O. Box 4120, 7411KB Zutphen - The Netherlands</p>
      <p class="best">Best used before the end of:</p>
    </div>
    <div class="pack__ingredients">
      <p>Ingredients</p>
      <p>Aqua, Aluminum Chlorohydrate, Propylene Glycol,<br>PEG-40 Hydrogenated Castor Oil, Ethylhexylglycerin,<br>Octenidine HCl, Phenoxyethanol, Parfum, Limonene.</p>
    </div>
    <div class="pack__date-slot"></div>
    <div class="seal" role="img" aria-label="Organic badge"></div>
  </section>

</main>
</body>
</html>
```